Website for Bramblewood Quarry Advisors

Please design a website that initially contains four or five pages. This work is for a newly formed consulting company, Bramblewood Quarry Advisors, that provides training and individual coaching to help business professionals and lawyers write more effectively and efficiently.

We work in a professional and conservative industry. The website should be simple, crisp, and clean.

I have attached a document that describes the four initial pages for the site: 1) a landing page, 2) a webpage that includes the pictures and bios of our two consultants, 3) a webpage that describes our services, and 4) a webpage that will contain a form that visitors can use to submit questions to us.

I also included the following files:
a. a powerpoint slide with our consultants' pictures and bios; and
b. our recently designed logo (jpg and png files).

Thank you!

```html
<!DOCTYPE html>
<html lang="en">
<head>
<meta charset="utf-8">
<title>Bramblewood Quarry Advisors</title>
<link href="https://fonts.googleapis.com/css2?family=Open+Sans:wght@400;600;700&family=Lato:wght@400;700&display=swap" rel="stylesheet">
<style>
:root{
  --navy:#1f2a5c;
  --navy-deep:#1a2250;
  --red:#c4232b;
  --ink:#1b1b1f;
  --muted:#7a7f8e;
  --light:#f5f6f8;
  --line:#e3e5ea;
  --white:#fff;
  --black:#0b0b0d;
}
*{box-sizing:border-box;margin:0;padding:0}
html,body{width:1200px;height:4696px;overflow:hidden}
body{position:relative;font-family:"Lato",sans-serif;color:var(--ink);background:var(--white)}
.abs{position:absolute}
h1,h2,h3,h4{font-family:"Open Sans",sans-serif}
.label{font-size:13px;color:var(--red);letter-spacing:.3px;text-transform:uppercase;text-decoration:underline;text-underline-offset:4px}
.btn{display:inline-flex;align-items:center;gap:14px;background:var(--red);color:#fff;font-family:"Open Sans",sans-serif;font-weight:600;font-size:16px;padding:0 22px;height:44px;border-radius:3px}
.btn svg{width:20px;height:14px}

/* top bar */
.topbar{top:0;left:0;width:1200px;height:40px;background:#fff;font-size:12px;color:var(--navy);font-weight:700}
.topbar .item{display:flex;align-items:center;gap:7px;top:12px}
.topbar .sq{width:11px;height:11px;border-radius:2px;background:#8a90aa}

/* hero */
.hero{top:40px;left:0;width:1200px;height:817px;overflow:hidden}
.hero-photo{position:absolute;inset:0;background:linear-gradient(180deg,#1e2a57 0%,#2e3654 18%,#4b4840 50%,#5b4e40 75%,#3a3a40 100%)}
.brand{color:#fff;font-family:"Open Sans",sans-serif;font-weight:600;font-size:17px;display:flex;align-items:center;gap:10px}
.brand .dot{width:12px;height:12px;border-radius:50%;background:#fff}
.badge{display:flex;align-items:center;gap:12px;color:#fff;font-size:12px;font-weight:700;line-height:1.3}
.badge .ring{width:22px;height:22px;border:2px solid var(--red);border-radius:50%}
.nav{top:84px;left:91px;width:996px;height:69px;background:#fff;border-radius:3px;box-shadow:0 4px 14px rgba(0,0,0,.15)}
.nav a{position:absolute;top:24px;font-size:15px;color:var(--navy);text-decoration:none}
.nav .active{border-bottom:4px solid var(--red);padding:0 24px 19px;left:121px}
.nav .quote{left:816px;top:16px;width:152px;height:40px;background:var(--red);color:#fff;border-radius:20px;font-size:13px;font-weight:700;text-align:center;line-height:40px;padding:0}
.hero-kicker{top:330px;width:1200px;text-align:center;color:#fff;font-size:13px;letter-spacing:.4px}
.hero-title{top:352px;width:1200px;text-align:center;color:#fff;font-size:58px;font-weight:700;line-height:77px}
.hero .btn{top:583px;left:552px;height:44px}

/* about */
.about-photo{top:957px;left:100px;width:438px;height:438px;border-radius:50%;background:linear-gradient(140deg,#2a3567 0%,#8d97a8 45%,#d8d6d0 70%,#3d3b44 100%)}
.about-ring{top:957px;left:96px;width:442px;height:438px;border-radius:50%;border-left:18px solid var(--navy)}
.about-badge{top:1287px;left:432px;width:104px;height:104px;border-radius:50%;background:#fff;box-shadow:0 4px 16px rgba(0,0,0,.15)}
.about-badge::after{content:"";position:absolute;left:40px;top:40px;width:24px;height:24px;border-radius:50%;background:var(--red)}
.about h2{font-size:40px;line-height:54px;font-weight:600;color:var(--ink)}
.about h3{font-size:22px;font-weight:400}
.about p{font-size:13px;line-height:22px;color:var(--muted);width:510px}

/* services */
.services{top:1446px;left:0;width:1200px;height:556px;background:var(--light)}
.center{width:1200px;text-align:center}
.section-title{font-size:40px;font-weight:600;color:var(--ink)}
.card{top:184px;width:314px;height:310px;background:#fff;border:1px solid var(--line);text-align:center}
.card h4{margin-top:134px;font-size:19px;font-weight:400;color:var(--navy)}
.card p{margin:30px auto 0;width:200px;font-size:13px;line-height:19px;color:var(--muted)}
.card svg{position:absolute;left:132px;top:58px;width:50px;height:50px}
.card.featured{background:linear-gradient(160deg,#3c3c44,#6a6a70 50%,#2a2a30);border:none;border-bottom:4px solid var(--red)}
.card.featured h4,.card.featured p{color:#fff}

/* call band */
.callband{top:2002px;left:0;width:1200px;height:306px;background:linear-gradient(100deg,#6d4a2c 0%,#8a5a32 35%,#5b4634 70%,#3e3a3a 100%)}
.callband h2{position:absolute;top:108px;width:1200px;text-align:center;color:#fff;font-size:34px;font-weight:600;line-height:42px}
.callband .accent{color:#1aa3d6}
.callbox{top:2275px;left:350px;width:501px;height:58px;background:#fff;border-radius:3px;box-shadow:0 6px 16px rgba(0,0,0,.12);display:flex;align-items:center;justify-content:space-around;font-size:16px;color:var(--navy)}

/* why */
.why{top:2333px;left:0;width:1200px;height:635px;background:var(--light)}
.hub{top:361px;left:472px;width:256px;height:256px;border:4px solid var(--navy);border-radius:50%}
.hub-core{top:401px;left:500px;width:200px;height:200px;border-radius:50%;background:#fff;box-shadow:0 0 24px rgba(0,0,0,.08)}
.node{width:14px;height:14px;border:2px solid var(--navy);border-radius:50%;background:#fff}
.icon{width:64px;height:64px;border-radius:50%;background:#fff;box-shadow:0 4px 14px rgba(0,0,0,.1);display:flex;align-items:center;justify-content:center}
.icon svg{width:30px;height:30px}
.point h4{font-size:20px;font-weight:400;color:var(--ink)}
.point p{font-size:13px;line-height:20px;color:var(--muted);margin-top:4px}
.point.left{text-align:right}

/* testimonials */
.reviews{top:2968px;left:0;width:1200px;height:623px;background:linear-gradient(120deg,#26272c,#3b3d44 50%,#1e1f24)}
.reviews .label{color:#fff}
.reviews .section-title{color:#fff}
.review{top:213px;width:312px;height:268px;border:1px solid #555;background:rgba(0,0,0,.35);text-align:center;color:#fff}
.review.light{background:#fff;border:none;border-bottom:4px solid var(--red);color:var(--ink)}
.review h4{margin-top:50px;font-size:16px;font-weight:700;color:inherit}
.review.light h4{color:var(--navy)}
.review p{margin:42px auto 0;width:250px;font-size:13px;line-height:19px}
.review.light p{color:var(--muted)}
.avatar{position:absolute;top:-36px;left:121px;width:70px;height:70px;border-radius:50%;background:linear-gradient(160deg,#d9c9be,#8c7868);border:3px solid #fff}
.dots{top:3493px;left:560px;display:flex;gap:8px;align-items:center}
.dots span{width:10px;height:10px;border:1px solid #fff;border-radius:50%}
.dots .on{width:22px;height:3px;border:none;background:#fff;border-radius:2px}

/* contact */
.contact-title{top:3654px;left:104px;font-size:40px;font-weight:600}
.contact-title span{font-weight:400}
.cinfo{left:112px;display:flex;gap:30px}
.cinfo svg{width:40px;height:40px}
.cinfo h5{font-size:13px;font-weight:700;color:var(--ink);margin-top:2px}
.cinfo p{font-size:13px;color:var(--muted);margin-top:4px}
.swoosh{top:4040px;left:0;width:1200px;height:656px}
.footer{top:4210px;left:0;width:1200px;height:486px;background:var(--black)}
.form{top:3655px;left:600px;width:494px;height:571px;background:#fff;border-top:6px solid var(--black);box-shadow:0 6px 26px rgba(0,0,0,.12);padding:34px 38px}
.form h3{font-size:24px;font-weight:600}
.form label{display:block;font-size:13px;font-weight:700;color:var(--ink)}
.field{height:42px;border:1px solid #b5b9c6;border-radius:21px;font-size:13px;color:#6a6f80;padding:12px 22px;margin-top:8px}
.field.area{height:124px;border-radius:14px}

/* footer */
.fbrand{top:4285px;left:128px}
.footer .txt{font-size:12px;line-height:22px;color:#8a8ea0}
.footer h5{font-size:14px;color:#fff;font-weight:700}
.social{display:flex;gap:10px}
.social span{width:28px;height:28px;border-radius:4px;background:#3a3a5a}
.social span:first-child{background:var(--red)}
.links a{display:block;font-size:12px;color:#8a8ea0;line-height:26px;text-decoration:none}
.nl{top:4376px;left:828px;display:flex}
.nl .in{width:194px;height:46px;background:#fff;font-size:12px;color:#555;padding:16px 24px}
.nl .go{width:54px;height:46px;background:var(--red);display:flex;align-items:center;justify-content:center}
.fc{display:flex;gap:14px;align-items:center}
.fc .ci{width:48px;height:48px;border-radius:50%;background:#2b2b55;display:flex;align-items:center;justify-content:center}
.fc .ci.red{background:var(--red)}
.fc .ci svg{width:20px;height:20px}
.fc h6{font-size:14px;color:#fff;font-family:"Lato",sans-serif;font-weight:700}
.fc p{font-size:11px;color:#6d7088;margin-top:4px}
.frule{top:4630px;left:128px;width:944px;height:1px;background:#2a2a30}
.copy{top:4664px;width:1200px;text-align:center;color:#fff;font-size:12px;font-weight:700}
</style>
</head>
<body>

<!-- top bar -->
<div class="abs topbar">
  <div class="abs item" style="left:90px"><svg width="13" height="13" viewBox="0 0 24 24"><path d="M6 2l4 4-2 3c1 3 4 6 7 7l3-2 4 4-3 4C10 22 2 14 2 5z" fill="#c4232b"/></svg>(+1) 555-014-2290</div>
  <div class="abs" style="left:240px;top:11px;color:#b0b4c2">|</div>
  <div class="abs item" style="left:254px"><svg width="14" height="11" viewBox="0 0 24 18"><rect width="24" height="18" rx="2" fill="#c4232b"/><path d="M1 2l11 8 11-8" stroke="#fff" stroke-width="2" fill="none"/></svg>hello@bramblewoodqa.com</div>
  <div class="abs" style="left:405px;top:11px;color:#b0b4c2">|</div>
  <div class="abs item" style="left:426px"><svg width="11" height="14" viewBox="0 0 16 22"><path d="M8 0a8 8 0 018 8c0 6-8 14-8 14S0 14 0 8a8 8 0 018-8z" fill="#c4232b"/><circle cx="8" cy="8" r="3" fill="#fff"/></svg>48 Quarry Lane</div>
  <div class="abs item" style="left:990px;gap:14px"><span class="sq"></span><span class="sq"></span><span class="sq"></span><span class="sq"></span></div>
</div>

<!-- hero -->
<section class="abs hero">
  <div class="hero-photo" role="img" aria-label="Team of consultants in a meeting around a conference table"></div>
  <div class="abs brand" style="top:38px;left:96px"><span class="dot"></span>Bramblewood Quarry Advisors</div>
  <div class="abs badge" style="top:28px;left:808px"><span class="ring"></span><span>24/7<br>Service</span></div>
  <div class="abs" style="top:26px;left:938px;width:1px;height:38px;background:#fff;opacity:.6"></div>
  <div class="abs badge" style="top:28px;left:966px"><span class="ring"></span><span>Qualified<br>Professionals</span></div>
  <nav class="abs nav">
    <a class="active">Home</a>
    <a style="left:197px">About Us</a>
    <a style="left:335px">Services</a>
    <a style="left:483px">Our Team</a>
    <a style="left:623px">Contact Us</a>
    <a class="quote">Get A Quote</a>
  </nav>
  <div class="abs hero-kicker">WRITING CONSULTANTS</div>
  <h1 class="abs hero-title">Words That Speak,<br>Strategies That Succeed</h1>
  <div class="abs btn">Contact us <svg viewBox="0 0 20 14"><path d="M1 7h17M12 1l6 6-6 6" stroke="#fff" stroke-width="2" fill="none"/></svg></div>
  <svg class="abs" style="left:0;top:0" width="1200" height="817" viewBox="0 0 1200 817">
    <path d="M0 635 C 320 760, 760 800, 1200 640 L1200 817 L0 817 Z" fill="#fff"/>
    <path d="M190 690 C 430 840, 800 850, 1135 695 C 860 885, 450 880, 190 690 Z" fill="#c4232b"/>
  </svg>
</section>

<!-- about -->
<section class="about">
  <div class="abs about-ring"></div>
  <div class="abs about-photo" role="img" aria-label="Senior consultant reviewing a laptop with a colleague"></div>
  <div class="abs about-badge"></div>
  <div class="abs label" style="top:966px;left:613px">Who we are</div>
  <h2 class="abs" style="top:998px;left:613px">Every Word Counts,<br>Every Message Matters</h2>
  <h3 class="abs" style="top:1130px;left:613px">Eloquent Expression, Profound Impression.</h3>
  <p class="abs" style="top:1175px;left:613px">Lorem ipsum dolor sit amet, consectetur adipiscing elit, sed do eiusmod tempor incididunt ut labore et dolore magna aliqua. Ut enim ad minim veniam, quis nos trud exercitation ullamco laboris nisi ut aliquip ex ea commodo consequat. Duis aute irure dolor in reprehenderit in voluptate velit esse cillum dolore eu fugiat nulla pariatur. Excepteur sint occaecat cupidatat non proident, sunt in culpa qui officia deserunt mollit anim id est laborum.</p>
  <div class="abs btn" style="top:1334px;left:613px">Contact us <svg viewBox="0 0 20 14"><path d="M1 7h17M12 1l6 6-6 6" stroke="#fff" stroke-width="2" fill="none"/></svg></div>
</section>

<!-- services -->
<section class="abs services">
  <div class="abs center label" style="top:44px">Our services</div>
  <h2 class="abs center section-title" style="top:76px">Services We Offer</h2>
  <div class="abs card featured" style="left:98px" role="img" aria-label="Consultant presenting a communication strategy">
    <svg viewBox="0 0 50 50"><rect x="8" y="30" width="6" height="14" fill="#fff"/><rect x="18" y="22" width="6" height="22" fill="#fff"/><circle cx="36" cy="14" r="5" fill="#fff"/><path d="M30 44V24h12v20" stroke="#fff" stroke-width="4" fill="none"/></svg>
    <h4>Communication Strategy</h4>
    <p>Lorem ipsum dolor sit amet, consectetur adipiscing elit, sed do eiusmod tempor</p>
  </div>
  <div class="abs card" style="left:441px">
    <svg viewBox="0 0 50 50"><circle cx="25" cy="9" r="5" fill="#c4232b"/><path d="M6 18h38M25 18v12M12 44l13-14 13 14" stroke="#c4232b" stroke-width="4" fill="none"/></svg>
    <h4>Technical Writing</h4>
    <p>Lorem ipsum dolor sit amet, consectetur adipiscing elit, sed do eiusmod tempor</p>
  </div>
  <div class="abs card" style="left:782px">
    <svg viewBox="0 0 50 50"><circle cx="25" cy="25" r="20" stroke="#c4232b" stroke-width="2" stroke-dasharray="3 3" fill="none"/><circle cx="25" cy="25" r="12" stroke="#c4232b" stroke-width="4" fill="none"/><circle cx="25" cy="25" r="5" fill="#c4232b"/></svg>
    <h4>Content Creation</h4>
    <p>Lorem ipsum dolor sit amet, consectetur adipiscing elit, sed do eiusmod tempor</p>
  </div>
</section>

<!-- call band -->
<section class="abs callband" role="img" aria-label="Hands joined together in warm light">
  <h2>We're on Call <span class="accent">24/7</span> to React Promptly to Your<br>Writing Needs</h2>
</section>
<div class="abs callbox"><span>+ (001) 555-018-4471</span><span>[or]</span><span>desk@bramblewoodqa.com</span></div>

<!-- why choose us -->
<section class="abs why">
  <div class="abs center label" style="top:51px">Why choose us</div>
  <h2 class="abs center section-title" style="top:90px">Why Choose Us</h2>
  <div class="abs hub"></div>
  <div class="abs hub-core"></div>
  <div class="abs node" style="left:520px;top:381px"></div>
  <div class="abs node" style="left:666px;top:381px"></div>
  <div class="abs node" style="left:463px;top:481px"></div>
  <div class="abs node" style="left:721px;top:481px"></div>
  <div class="abs node" style="left:516px;top:583px"></div>
  <div class="abs node" style="left:668px;top:583px"></div>

  <div class="abs icon" style="left:436px;top:220px"><svg viewBox="0 0 30 30"><path d="M5 15a10 10 0 0120 0M25 15a10 10 0 01-20 0" stroke="#c4232b" stroke-width="3" fill="none"/><path d="M10 15h10" stroke="#c4232b" stroke-width="3"/></svg></div>
  <div class="abs icon" style="left:375px;top:329px"><svg viewBox="0 0 30 30"><circle cx="9" cy="9" r="4" fill="#c4232b"/><path d="M2 22a7 7 0 0114 0z" fill="#c4232b"/><path d="M18 8h10M18 14h10M18 20h10" stroke="#c4232b" stroke-width="3"/></svg></div>
  <div class="abs icon" style="left:426px;top:433px"><svg viewBox="0 0 30 30"><circle cx="15" cy="15" r="11" stroke="#c4232b" stroke-width="3" fill="none" stroke-dasharray="5 2"/><path d="M10 15l4 4 7-8" stroke="#c4232b" stroke-width="3" fill="none"/></svg></div>
  <div class="abs icon" style="left:700px;top:220px"><svg viewBox="0 0 30 30"><path d="M25 15A10 10 0 1115 5" stroke="#c4232b" stroke-width="3" fill="none"/><path d="M15 1l5 4-5 4" fill="#c4232b"/></svg></div>
  <div class="abs icon" style="left:757px;top:329px"><svg viewBox="0 0 30 30"><rect x="4" y="20" width="4" height="7" fill="#c4232b"/><rect x="11" y="15" width="4" height="12" fill="#c4232b"/><circle cx="22" cy="7" r="3" fill="#c4232b"/><rect x="19" y="12" width="6" height="15" fill="#c4232b"/></svg></div>
  <div class="abs icon" style="left:708px;top:433px"><svg viewBox="0 0 30 30"><rect x="3" y="3" width="8" height="8" stroke="#c4232b" stroke-width="3" fill="none"/><rect x="19" y="19" width="8" height="8" stroke="#c4232b" stroke-width="3" fill="none"/><path d="M11 7h10v12M19 23H7V11" stroke="#c4232b" stroke-width="3" fill="none"/></svg></div>

  <div class="abs point left" style="right:840px;top:213px"><h4>Client Centric</h4><p>Lorem ipsum dolor sit amet,<br>consectetur adipiscing elit,</p></div>
  <div class="abs point left" style="right:866px;top:331px;text-align:left"><h4>Proffesionalism</h4><p>Lorem ipsum dolor sit amet,<br>consectetur adipiscing elit,</p></div>
  <div class="abs point left" style="right:840px;top:438px"><h4 style="text-align:left">Customized Solutions</h4><p>Lorem ipsum dolor sit amet,<br>consectetur adipiscing elit,</p></div>
  <div class="abs point" style="left:836px;top:213px"><h4>Continuous Monitoring</h4><p>Lorem ipsum dolor sit amet,<br>consectetur adipiscing elit,</p></div>
  <div class="abs point" style="left:874px;top:331px"><h4>Empathetic Staff</h4><p>Lorem ipsum dolor sit amet,<br>consectetur adipiscing elit,</p></div>
  <div class="abs point" style="left:836px;top:438px"><h4>Flexible Services</h4><p>Lorem ipsum dolor sit amet,<br>consectetur adipiscing elit,</p></div>
</section>

<!-- testimonials -->
<section class="abs reviews" role="img" aria-label="Professionals collaborating in an office, darkened">
  <div class="abs center label" style="top:52px">Testimonials</div>
  <h2 class="abs center section-title" style="top:86px">Clients' Reviews</h2>
  <div class="abs review light" style="left:95px"><div class="avatar"></div><h4>Daniel Harrow</h4><p>Lorem ipsum dolor sit amet, consectetur adipiscing elit Lorem ipsum dolor sit amet, consectetur adipiscing elit</p></div>
  <div class="abs review" style="left:434px"><div class="avatar"></div><h4>Daniel Harrow</h4><p>Lorem ipsum dolor sit amet, consectetur adipiscing elit Lorem ipsum dolor sit amet, consectetur adipiscing elit</p></div>
  <div class="abs review" style="left:774px"><div class="avatar"></div><h4>Daniel Harrow</h4><p>Lorem ipsum dolor sit amet, consectetur adipiscing elit Lorem ipsum dolor sit amet, consectetur adipiscing elit</p></div>
</section>
<div class="abs dots"><span></span><span class="on"></span><span></span></div>

<!-- contact -->
<h2 class="abs contact-title">Contact Us <span>Today</span></h2>
<div class="abs cinfo" style="top:3728px"><svg viewBox="0 0 40 40"><path d="M20 4a9 9 0 019 9c0 7-9 15-9 15s-9-8-9-15a9 9 0 019-9z" stroke="#c4232b" stroke-width="2" fill="none"/><circle cx="20" cy="13" r="3" fill="#c4232b"/><path d="M4 36l8-10h16l8 10z" stroke="#1f2a5c" stroke-width="2" fill="none"/></svg><div><h5>HEAD OFFICE</h5><p>21 Lorem Ipsum, ABC 123</p></div></div>
<div class="abs cinfo" style="top:3801px"><svg viewBox="0 0 40 40"><rect x="4" y="10" width="32" height="24" rx="2" stroke="#c4232b" stroke-width="2" fill="none"/><path d="M4 12l16 12 16-12" stroke="#1f2a5c" stroke-width="2" fill="none"/></svg><div><h5>EMAIL ADDRESS</h5><p>21 Lorem Ipsum, ABC 123</p></div></div>
<div class="abs cinfo" style="top:3866px"><svg viewBox="0 0 40 40"><rect x="12" y="4" width="16" height="32" rx="3" stroke="#c4232b" stroke-width="2" fill="none"/><path d="M18 31h4" stroke="#1f2a5c" stroke-width="2"/></svg><div><h5>CALL US NOW</h5><p>21 Lorem Ipsum, ABC 123</p></div></div>

<svg class="abs swoosh" viewBox="0 0 1200 656">
  <path d="M60 155 C 250 40, 450 20, 620 60 L620 75 C 450 45, 260 70, 60 155 Z" fill="#c4232b"/>
</svg>
<footer class="abs footer">
  <svg class="abs" style="left:0;top:-110px" width="1200" height="112" viewBox="0 0 1200 112"><path d="M0 112 L0 100 C 150 30, 350 0, 620 10 L1200 10 L1200 112 Z" fill="#0b0b0d"/></svg>
</footer>

<div class="abs form">
  <h3>Send Us A Message</h3>
  <div style="display:flex;gap:16px;margin-top:40px">
    <div style="flex:1"><label>First Name</label><div class="field">John</div></div>
    <div style="flex:1"><label>Last Name</label><div class="field">Doe</div></div>
  </div>
  <div style="margin-top:26px"><label>Email</label><div class="field">hello@bramblewoodqa.com</div></div>
  <div style="margin-top:26px"><label>Message</label><div class="field area">Type Your Message</div></div>
  <div class="btn" style="margin-top:40px">Contact us <svg viewBox="0 0 20 14"><path d="M1 7h17M12 1l6 6-6 6" stroke="#fff" stroke-width="2" fill="none"/></svg></div>
</div>

<!-- footer content -->
<div class="abs fbrand brand" style="color:#fff;font-size:17px"><span class="dot"></span>Bramblewood Quarry Advisors</div>
<p class="abs txt" style="top:4340px;left:128px;width:290px;font-size:11px;color:#5b5f88;line-height:20px">Lorem ipsum dolor sit amet, consectetur adipiscing elit, sed do eiusmod tempor incididunt ut</p>
<div class="abs social" style="top:4420px;left:128px"><span></span><span></span><span></span><span></span></div>
<h5 class="abs" style="top:4276px;left:492px;color:#fff;font-size:14px">Quick Links</h5>
<div class="abs links" style="top:4316px;left:492px"><a>Home</a><a>Services</a><a>About Us</a><a>Contact</a><a>Blog</a><a>Testimonials</a></div>
<div class="abs links" style="top:4316px;left:627px"><a>Cookies Policy</a><a>Terms of Use</a><a>Careers</a><a>Our Team</a><a>More</a></div>
<h5 class="abs" style="top:4276px;left:828px;color:#fff;font-size:14px">Newsletters</h5>
<p class="abs" style="top:4312px;left:828px;width:250px;font-size:11px;line-height:20px;color:#5b5f88">Lorem ipsum dolor sit amet, consectetur adipi elit, sed do eiusmod tempor incididunt ut</p>
<div class="abs nl"><div class="in">Enter Email Address</div><div class="go"><svg width="12" height="18" viewBox="0 0 12 18"><path d="M2 2l7 7-7 7" stroke="#fff" stroke-width="3" fill="none"/></svg></div></div>

<div class="abs fc" style="top:4528px;left:128px"><div class="ci"><svg viewBox="0 0 16 22"><path d="M8 0a8 8 0 018 8c0 6-8 14-8 14S0 14 0 8a8 8 0 018-8z" fill="#8a8ec0"/></svg></div><div><h6>Address</h6><p>48 Quarry Lane</p></div></div>
<div class="abs fc" style="top:4528px;left:366px"><div class="ci red"><svg viewBox="0 0 24 18"><rect width="24" height="18" rx="2" fill="#fff"/><path d="M1 2l11 8 11-8" stroke="#c4232b" stroke-width="2" fill="none"/></svg></div><div><h6>Email Us</h6><p>support@bramblewoodqa.com</p></div></div>
<div class="abs fc" style="top:4528px;left:632px"><div class="ci"><svg viewBox="0 0 24 24"><path d="M6 2l4 4-2 3c1 3 4 6 7 7l3-2 4 4-3 4C10 22 2 14 2 5z" fill="#8a8ec0"/></svg></div><div><h6>Contact Us</h6><p>+012(5550) 143 27</p></div></div>
<div class="abs fc" style="top:4528px;left:860px"><div class="ci"><svg viewBox="0 0 24 24"><circle cx="12" cy="12" r="9" stroke="#8a8ec0" stroke-width="2" fill="none"/><path d="M12 7v5l3 3" stroke="#8a8ec0" stroke-width="2" fill="none"/></svg></div><div><h6>Opening Hour</h6><p>Mon - Friday: 10 am - 8pm</p></div></div>
<div class="abs frule"></div>
<div class="abs copy">Bramblewood Quarry Advisors</div>

</body>
</html>
```